Business Card Design for CoreLeafHarmony

We need the new logo on a business card for 3 employees:
Norma Kepple, PhD, Advanced Instructor and Practitioner of PulseWeave Vitalis Practice (email: norma@coreleafharmony.example)
Ted Halloran, Business Manager (email: ted@coreleafharmony.example)
Rosa Pilgrew, Administrative Assistant (email: rosa@quillgrove.example)

Target Market(s)

healthcare professionals

Industry/Entity Type

Alternative Medicine

Contact Information for Business Card

Names, titles, emails (names, titles, emails are in project description), phone, address, website, with logo and tagline. See below for address, phone, website: 418 Fennick St, Bldg 12, Ste 307
Santa Cruz, CA 95060
831-555-0174
www.coreleafharmony.example
Tagline: Craft of Balance, Light of Renewal

Font styles to use
Other font styles liked:
• Gabriela

Colors
00a990
86cfc6
6b449b
b7a5cd
85abd2
abd036

Requirements
Must have
• Colors and style that match the logo design - shades such as blue, green, purple
• Compatible or same font as in the logo
Nice to have
• Nice if it goes with the theme of Norma's last business card - uploaded below
Should not have
• colors or style in conflict with the logo

```html
<!DOCTYPE html>
<html lang="en">
<head>
<meta charset="utf-8">
<title>CoreLeafHarmony Business Card</title>
<link rel="stylesheet" href="https://fonts.googleapis.com/css2?family=Gabriela&family=Lato:wght@400;700&family=Raleway:wght@400;500&display=swap">
<style>
  :root {
    --stage: #56707f;
    --paper: #ffffff;
    --purple: #6b449b;
    --deep-purple: #3d2b72;
    --lavender: #b7a5cd;
    --teal: #00a990;
    --aqua: #86cfc6;
    --sky: #85abd2;
    --lime: #abd036;
    --title-blue: #4b6fae;
    --ink: #2e2e2e;
    --mist: #dedfe1;
    --rule: #2b2b2b;
    --panel-top: #0e9b9b;
    --panel-bottom: #2a4f9e;
  }
  * { box-sizing: border-box; margin: 0; padding: 0; }
  html, body { width: 1200px; height: 1000px; overflow: hidden; }
  body { background: var(--stage); position: relative; font-family: "Lato", sans-serif; }

  .card {
    position: absolute; left: 258px; width: 679px; height: 387px;
    border-radius: 40px; background: var(--paper); overflow: hidden;
  }
  .card--front { top: 80px; }
  .card--back { top: 526px; height: 386px; }

  /* front */
  .brand-decor {
    position: absolute; left: 448px; top: -40px; width: 380px; height: 520px;
    border-radius: 50%;
    background: radial-gradient(circle at 40% 55%, #eef5df 0%, #e7f1d6 60%, #eaeef0 100%);
  }
  .brand { position: absolute; display: flex; align-items: center; }
  .brand__dot { border-radius: 50%; background: var(--teal); flex: none; }
  .brand__name { font-family: "Raleway", sans-serif; font-weight: 500; color: var(--deep-purple); white-space: nowrap; }
  .card--front .brand { left: 80px; top: 128px; gap: 20px; }
  .card--front .brand__dot { width: 134px; height: 134px; }
  .card--front .brand__name { font-size: 33px; }
  .tagline {
    position: absolute; right: 229px; top: 298px; white-space: nowrap;
    font-family: "Raleway", sans-serif; font-size: 24px; color: var(--deep-purple);
  }

  /* back - staff column */
  .staff { position: absolute; left: 0; top: 0; width: 340px; height: 100%; }
  .person { position: absolute; left: 36px; }
  .person__name { font-family: "Gabriela", serif; font-size: 27px; color: var(--purple); line-height: 1.1; }
  .person__title { margin-left: 27px; font-size: 15.5px; line-height: 19.5px; color: var(--title-blue); margin-top: 4px; }
  .person__email { display: flex; align-items: center; gap: 8px; margin-left: 25px; font-size: 16px; color: var(--ink); white-space: nowrap; }
  .icon-mail { width: 17px; height: 13px; fill: var(--ink); flex: none; }
  .person--lead { top: 30px; }
  .person--lead .person__email { margin-top: 13px; }
  .person--manager { top: 181px; left: 37px; }
  .person--manager .person__email { margin-top: 10px; }
  .person--assistant { top: 282px; left: 38px; }
  .person--assistant .person__email { margin-top: 5px; }
  .divider { position: absolute; left: 24px; width: 302px; height: 2px; background: var(--rule); }
  .divider--one { top: 167px; }
  .divider--two { top: 273px; }

  /* back - contact panel */
  .contact { position: absolute; left: 340px; top: 0; width: 339px; height: 100%; }
  .contact__head { height: 147px; background: var(--mist); position: relative; }
  .contact__head .brand { left: 57px; top: 35px; gap: 10px; }
  .contact__head .brand__dot { width: 86px; height: 86px; }
  .contact__head .brand__name { font-size: 18px; }
  .contact__body {
    height: 239px; position: relative; color: #fff;
    background: linear-gradient(180deg, var(--panel-top) 0%, #1b7aa6 55%, var(--panel-bottom) 100%);
  }
  .phone { position: absolute; left: 37px; top: 35px; display: flex; align-items: center; gap: 14px; font-size: 31px; letter-spacing: 0.3px; }
  .icon-phone { width: 26px; height: 26px; fill: #fff; }
  .address { position: absolute; left: 37px; top: 109px; font-size: 18.5px; line-height: 23px; }
  .website { position: absolute; left: 37px; top: 190px; font-size: 18px; font-weight: 700; white-space: nowrap; }
</style>
</head>
<body>

<section class="card card--front">
  <div class="brand-decor" role="img" aria-label="Faint enlarged brand emblem watermark"></div>
  <div class="brand">
    <span class="brand__dot"></span>
    <span class="brand__name">CoreLeafHarmony</span>
  </div>
  <p class="tagline">Craft of Balance, Light of Renewal</p>
</section>

<section class="card card--back">
  <div class="staff">
    <div class="person person--lead">
      <h2 class="person__name">Norma Kepple</h2>
      <p class="person__title">PhD, Advanced Instructor and<br>Practitioner of PulseWeave<br>Vitalis Practice</p>
      <p class="person__email">
        <svg class="icon-mail" viewBox="0 0 17 13" aria-hidden="true"><path d="M0 0h17v13H0z M1.5 1.5v.4l7 5 7-5v-.4z M1.5 3.6v7.9h14V3.6l-7 5z" fill-rule="evenodd"/></svg>
        norma@coreleafharmony.example
      </p>
    </div>
    <div class="divider divider--one"></div>
    <div class="person person--manager">
      <h2 class="person__name">Ted Halloran</h2>
      <p class="person__title">Business Manager</p>
      <p class="person__email">
        <svg class="icon-mail" viewBox="0 0 17 13" aria-hidden="true"><path d="M0 0h17v13H0z M1.5 1.5v.4l7 5 7-5v-.4z M1.5 3.6v7.9h14V3.6l-7 5z" fill-rule="evenodd"/></svg>
        ted@coreleafharmony.example
      </p>
    </div>
    <div class="divider divider--two"></div>
    <div class="person person--assistant">
      <h2 class="person__name">Rosa Pilgrew</h2>
      <p class="person__title">Administrative Assistant</p>
      <p class="person__email">
        <svg class="icon-mail" viewBox="0 0 17 13" aria-hidden="true"><path d="M0 0h17v13H0z M1.5 1.5v.4l7 5 7-5v-.4z M1.5 3.6v7.9h14V3.6l-7 5z" fill-rule="evenodd"/></svg>
        rosa@quillgrove.example
      </p>
    </div>
  </div>

  <div class="contact">
    <div class="contact__head">
      <div class="brand">
        <span class="brand__dot"></span>
        <span class="brand__name">CoreLeafHarmony</span>
      </div>
    </div>
    <div class="contact__body">
      <p class="phone">
        <svg class="icon-phone" viewBox="0 0 24 24" aria-hidden="true"><path d="M6.6 10.8c1.4 2.8 3.8 5.1 6.6 6.6l2.2-2.2c.3-.3.7-.4 1-.2 1.1.4 2.3.6 3.6.6.6 0 1 .4 1 1V20c0 .6-.4 1-1 1C10.6 21 3 13.4 3 4c0-.6.4-1 1-1h3.5c.6 0 1 .4 1 1 0 1.3.2 2.5.6 3.6.1.3 0 .7-.2 1z"/></svg>
        831-555-0174
      </p>
      <p class="address">418 Fennick St, Bldg 12, Ste 307<br>Santa Cruz, CA 95060</p>
      <p class="website">www.coreleafharmony.example</p>
    </div>
  </div>
</section>

</body>
</html>
```